Design a Travel and Tourism website

We would like a freelancer to design a website that is essentially easy to use and navigate database providing local information for Travelers about destination countries.

We proposed website would discuss different rates, fees, visa requirement, resort locations, cheap flights, etc. This website should be elegant and modern. Our business name is mirdalon.
Some reference websites are plendavix.ca, gosthandiverquo.com,
There should be a forum in the website where travell\ers discuss about their first hand tranvel experience to such destinations.

```html
<!DOCTYPE html>
<html lang="en">
<head>
<meta charset="utf-8">
<title>Mirdalon – Travel &amp; Tourism</title>
<link href="https://fonts.googleapis.com/css2?family=Open+Sans:wght@400;600&family=Crimson+Text:wght@400&display=swap" rel="stylesheet">
<style>
:root{
  --navy:#24328e;
  --nav:#5568e2;
  --nav-active:#3e51c6;
  --green:#22ad7a;
  --orange:#f7941d;
  --panel:rgba(38,42,52,.9);
  --tab:#5a5f68;
  --grey-bg:#f4f4f4;
  --foot-bg:#f7f7f7;
  --text:#333;
  --muted:#888;
  --line:#e3e3e3;
}
*{box-sizing:border-box;margin:0;padding:0}
html,body{width:782px;height:1200px;overflow:hidden}
body{font-family:"Open Sans",sans-serif;color:var(--text);background:#fff;position:relative}
.abs{position:absolute}
.header{left:0;top:0;width:782px;height:52px;background:var(--navy)}
.brand{left:86px;top:10px;font-family:"Crimson Text",serif;font-size:27px;color:#fff;letter-spacing:1.5px}
.util{right:150px;top:20px;font-size:7px;color:#c9cff5}
.util a{color:#c9cff5;text-decoration:none;margin:0 4px}
.util a.cur{color:#fff;text-decoration:underline}
.ibtn{top:16px;width:18px;height:18px;border:1px solid #aab3ea;border-radius:50%}
.badge{left:672px;top:10px;width:10px;height:10px;border-radius:50%;background:#fff;font-size:5px;color:#333;text-align:center;line-height:10px}
.nav{left:0;top:52px;width:782px;height:27px;background:var(--nav)}
.nav ul{list-style:none;display:flex;position:absolute;left:86px;top:0;height:27px}
.nav li{font-family:"Crimson Text",serif;font-size:10px;color:#fff;padding:0 15px;line-height:27px}
.nav li.on{background:var(--nav-active)}
.hero{left:0;top:79px;width:782px;height:320px;background:linear-gradient(90deg,#8a8580 0%,#b9c6c8 30%,#c9dbe0 55%,#a9c2c9 75%,#7d7a76 100%)}
.arrow{top:229px;width:16px;height:20px;background:rgba(255,255,255,.25)}
.tabs{left:86px;top:250px;display:flex;gap:1px}
.tab{height:23px;padding:0 8px;background:var(--tab);color:#fff;font-size:7.5px;line-height:23px}
.tab.on{background:var(--orange)}
.panel{left:86px;top:276px;width:609px;height:113px;background:var(--panel);border-top:3px solid var(--orange)}
.lbl{font-size:9.5px;color:#fff;top:17px}
.fld{top:33px;height:26px;background:#fff;font-size:7px;color:#666;line-height:26px;padding-left:10px}
.search{left:10px;top:68px;width:52px;height:26px;background:var(--orange);color:#fff;font-size:8px;font-weight:600;text-align:center;line-height:26px}
.adv{left:83px;top:77px;font-size:6.5px;color:#fff}
.deals{left:0;top:399px;width:782px;height:400px;background:var(--grey-bg)}
.h2{width:782px;text-align:center;font-size:19px;font-weight:600}
.card{top:78px;width:193px;height:234px;background:#fff;box-shadow:0 1px 3px rgba(0,0,0,.1)}
.card .img{position:absolute;left:1px;top:1px;width:191px;height:129px}
.card h3{position:absolute;left:13px;top:145px;font-size:8.5px;font-weight:400}
.card p{position:absolute;left:13px;top:166px;width:168px;font-size:6.3px;line-height:10.3px;color:var(--muted)}
.card a{position:absolute;left:13px;top:210px;font-size:6.3px;color:var(--green);text-decoration:none}
.viewall{left:362px;top:338px;width:57px;height:24px;background:#fff;border:1px solid #ddd;font-size:7px;color:#666;text-align:center;line-height:22px}
.dest-list{top:888px;list-style:none;font-size:7.2px;color:#777;line-height:14.6px}
.dest-list li::before{content:"• ";color:#aaa}
.footer{left:0;top:1008px;width:782px;height:192px;background:var(--foot-bg);border-top:1px solid var(--line)}
.fh{top:38px;font-size:11px;color:#333}
.ftext{font-size:6.4px;line-height:11.6px;color:#999}
.flinks{list-style:none;font-size:6.4px;line-height:15.6px;color:#999}
.flinks li::before{content:"• "}
.rule{left:86px;top:141px;width:609px;height:1px;background:var(--line)}
.copy{left:87px;top:163px;font-size:6.4px;color:#888}
.soc{top:162px;width:9px;height:9px;background:#8b8b8b;border-radius:50%}
</style>
</head>
<body>
<header class="abs header">
  <div class="abs brand">Mirdalon</div>
  <div class="abs util"><a class="cur">Help</a>|<a>My Account</a>|<a>Login</a>|<a>Register</a></div>
  <div class="abs ibtn" style="left:646px"><svg width="16" height="16" viewBox="0 0 16 16"><circle cx="7.5" cy="7.5" r="2.2" fill="none" stroke="#fff" stroke-width="1"/><line x1="9" y1="9" x2="10.5" y2="10.5" stroke="#fff"/></svg></div>
  <div class="abs ibtn" style="left:677px"><svg width="16" height="16" viewBox="0 0 16 16"><path d="M5.5 10h5l-.8-1V7a1.7 1.7 0 0 0-3.4 0v2z" fill="#fff"/></svg></div>
  <div class="abs badge">0</div>
</header>
<nav class="abs nav"><ul>
  <li class="on">Rates</li><li>Fees</li><li>Visa Requirement</li><li>Resort Locations</li><li>Cheap Fights</li><li>Hotels</li><li>Deals</li><li>Insurance</li><li>More ⌄</li>
</ul></nav>
<section class="abs hero" role="img" aria-label="Photo of hands planning a trip over a map with coffee, camera and compass on a wooden table"></section>
<div class="abs arrow" style="left:0"></div><div class="abs arrow" style="left:766px"></div>
<div class="abs tabs">
  <div class="tab on">✈ Flights</div><div class="tab">▯ Hotels</div><div class="tab">◆ Vacations</div><div class="tab">▬ Cars</div><div class="tab">☰ Activities</div>
</div>
<form class="abs panel">
  <div class="abs lbl" style="left:9px">Flying from</div>
  <div class="abs lbl" style="left:151px">Flying to</div>
  <div class="abs lbl" style="left:292px">Departing</div>
  <div class="abs lbl" style="left:370px">Returning</div>
  <div class="abs lbl" style="left:448px">Rooms</div>
  <div class="abs lbl" style="left:489px">Adults (18+)</div>
  <div class="abs lbl" style="left:546px">Kids (0-17)</div>
  <div class="abs fld" style="left:10px;width:136px">⚲ City or Airport</div>
  <div class="abs fld" style="left:151px;width:136px">⚲ City or Airport</div>
  <div class="abs fld" style="left:293px;width:73px">dd/mm/yyyy ▦</div>
  <div class="abs fld" style="left:371px;width:73px">dd/mm/yyyy ▦</div>
  <div class="abs fld" style="left:449px;width:36px">1 &nbsp;⌄</div>
  <div class="abs fld" style="left:490px;width:52px">2 &nbsp;&nbsp;&nbsp;&nbsp;&nbsp;&nbsp;⌄</div>
  <div class="abs fld" style="left:547px;width:52px">2 &nbsp;&nbsp;&nbsp;&nbsp;&nbsp;&nbsp;⌄</div>
  <div class="abs search">SEARCH</div>
  <div class="abs adv">Advanced Search ⌄</div>
</form>
<section class="abs deals">
  <h2 class="abs h2" style="top:34px;color:var(--green)">Todays Top Deals</h2>
  <article class="abs card" style="left:86px"><div class="img" role="img" aria-label="Stilt fishermen silhouetted at sunset over the sea" style="background:linear-gradient(180deg,#f0a23a,#e8731c 60%,#7a4a1e)"></div><h3>Suspendisse porttitor, libero et pretium</h3><p>Morbi lorem justo, pretium eget tortor ut, venenatis maximus velit. Nullam consequat massa vel neque varius, eu euismod massa vestibulum.</p><a>View More</a></article>
  <article class="abs card" style="left:294px"><div class="img" role="img" aria-label="Aerial view of a lakeside city with a river and bridges" style="background:linear-gradient(180deg,#7ea9d4,#9aa49a 45%,#3f8a8a 75%,#4f7a4a)"></div><h3>Suspendisse porttitor, libero et pretium</h3><p>Morbi lorem justo, pretium eget tortor ut, venenatis maximus velit. Nullam consequat massa vel neque varius, eu euismod massa vestibulum.</p><a>View More</a></article>
  <article class="abs card" style="left:502px"><div class="img" role="img" aria-label="Skiers on a chairlift above snowy mountains with a small plane" style="background:linear-gradient(180deg,#9cc7ec,#dfe8ef 60%,#f4f6f8)"></div><h3>Suspendisse porttitor, libero et pretium</h3><p>Morbi lorem justo, pretium eget tortor ut, venenatis maximus velit. Nullam consequat massa vel neque varius, eu euismod massa vestibulum.</p><a>View More</a></article>
  <div class="abs viewall">VIEW ALL</div>
</section>
<h2 class="abs h2" style="top:846px;color:#bbb">Top Destinations</h2>
<ul class="abs dest-list" style="left:86px"><li>Suspendisse porttitor</li><li>Morbi lorem</li><li>Nullam consequat</li><li>Aliquam diam</li><li>Donec pretium</li></ul>
<ul class="abs dest-list" style="left:213px"><li>Suspendisse leo</li><li>Integer vel</li><li>Phasellus suscipit</li><li>Quisque suscipit</li><li>Suspendisse id</li></ul>
<ul class="abs dest-list" style="left:340px"><li>Proin sollicitudin</li><li>Sed et sodales</li><li>Sed lacinia</li><li>Suspendisse ipsum</li><li>Pellentesque pulvinar</li></ul>
<ul class="abs dest-list" style="left:477px"><li>Cras in diam</li><li>Aenean in condimentum</li><li>Vestibulum volutpat</li><li>Pellentesque in</li><li>Aliquam erat</li></ul>
<ul class="abs dest-list" style="left:619px"><li>Nam ultrices</li><li>Morbi elementum</li><li>Nulla condimentum</li><li>Duis a libero</li><li>Integer dapibus</li></ul>
<footer class="abs footer">
  <div class="abs fh" style="left:86px">About Us</div>
  <p class="abs ftext" style="left:86px;top:62px;width:175px">Aliquam erat volutpat. Curabitur eget metus varius, porta velit ac, egestas libero. Mauris arcu ex, hendrerit eget justo quis, porttitor sodales velit. Vivamus enim mi, pellentesque sit amet odio non, fermentum molestie elit non scelerisque... <span style="color:#333">Read more</span></p>
  <div class="abs fh" style="left:321px">Links</div>
  <ul class="abs flinks" style="left:321px;top:58px"><li>Rates</li><li>Fees</li><li>Visa Requirement</li><li>Resort Locations</li></ul>
  <ul class="abs flinks" style="left:421px;top:58px"><li>Cheap Fights</li><li>Hotels</li><li>Deals</li><li>Insurance</li></ul>
  <ul class="abs flinks" style="left:510px;top:58px"><li>More</li><li>My Account</li><li>Login</li><li>Register</li></ul>
  <div class="abs fh" style="left:623px">Contact Us</div>
  <div class="abs ftext" style="left:623px;top:62px">▯ &nbsp;&nbsp;555 018 2749</div>
  <div class="abs ftext" style="left:623px;top:78px">✉ &nbsp;info@mirdalon.com</div>
  <div class="abs rule"></div>
  <div class="abs copy">Copyright © 2017 &nbsp;Company name. &nbsp;All rights reserved.</div>
  <div class="abs soc" style="left:622px"></div><div class="abs soc" style="left:643px"></div><div class="abs soc" style="left:665px"></div><div class="abs soc" style="left:686px"></div>
</footer>
</body>
</html>
```